Band Needs Quick Turnaround on CD Cover Text Placement

We have a great image for our cover. We need an expert at making the band name and title look fantastic. Please submit your ideas asap as we are on a time crunch to launch a crowd funding campaign. All we need is the cover design for now.

Target Market(s)

music fans who love rock, classic rock, americana, roots rock

Industry/Entity Type

Music Download

Font styles to use
Sans Serif

Colors
ffffff

Requirements
Must have
• The Band Name:
• Ray Kettleby & Iron Cloud Drifters
• (text should all be the same size) should be near the top right side of the design.
• The Album title:
• All Roads Bend Low
• Text Color: White or something close to white.
Should not have
• Other images or other font colors

```html
<!DOCTYPE html>
<html lang="en">
<head>
<meta charset="utf-8">
<title>Ray Kettleby &amp; Iron Cloud Drifters — All Roads Bend Low</title>
<link href="https://fonts.googleapis.com/css2?family=Josefin+Sans:wght@300;400&display=swap" rel="stylesheet">
<style>
  :root {
    --bg: #000000;
    --ink: #ffffff;
    --photo-light: #8a8a8a;
    --photo-mid: #4a4a4a;
    --photo-dark: #1a1a1a;
  }
  * { margin: 0; padding: 0; box-sizing: border-box; }
  html, body {
    width: 1200px;
    height: 931px;
    overflow: hidden;
    background: var(--bg);
  }
  .cover {
    position: relative;
    width: 1200px;
    height: 931px;
    background: var(--bg);
    overflow: hidden;
    font-family: "Josefin Sans", sans-serif;
  }
  .cover-photo {
    position: absolute;
    left: 0;
    top: 0;
    width: 770px;
    height: 931px;
    background:
      radial-gradient(ellipse 70% 55% at 30% 40%, var(--photo-light) 0%, var(--photo-mid) 45%, var(--photo-dark) 80%, transparent 100%),
      radial-gradient(ellipse 60% 45% at 55% 35%, var(--photo-mid) 0%, var(--photo-dark) 60%, transparent 100%);
  }
  .outline-text {
    color: transparent;
    -webkit-text-stroke: 1.6px var(--ink);
    text-transform: uppercase;
    font-weight: 400;
    text-align: right;
    line-height: 1;
  }
  .band-name {
    position: absolute;
    right: 26px;
    top: 72px;
  }
  .band-name .line {
    display: block;
    font-size: 64px;
    letter-spacing: 1px;
  }
  .band-name .line + .line { margin-top: 6px; }
  .band-name .amp {
    display: block;
    font-size: 30px;
    font-weight: 300;
    text-align: center;
    margin: 6px 0 6px 0;
    padding-left: 150px;
    -webkit-text-stroke: 1.2px var(--ink);
  }
  .album-title {
    position: absolute;
    right: 32px;
    top: 715px;
  }
  .album-title .line {
    display: block;
    font-size: 112px;
    font-weight: 300;
    letter-spacing: 2px;
    -webkit-text-stroke: 1.4px var(--ink);
  }
  .album-title .line + .line { margin-top: 2px; }
</style>
</head>
<body>
  <main class="cover">
    <div class="cover-photo" role="img" aria-label="Black and white close-up photograph of an elephant's head, ear and tusk against black"></div>

    <h1 class="band-name outline-text">
      <span class="line">Ray Kettleby</span>
      <span class="amp">&amp;</span>
      <span class="line">Iron Cloud</span>
      <span class="line">Drifters</span>
    </h1>

    <h2 class="album-title outline-text">
      <span class="line">All Roads</span>
      <span class="line">Bend Low</span>
    </h2>
  </main>
</body>
</html>
```